Cigar Ring Design

we are working on a project, which is an eCommerce store for cigars, now instead of selling all kind of existing brands this project is based on a TabacoMillDepot concept where an outlet is linked to an actual Cigar factory,
so the cigar lines sold will come out under a TMD (TabacoMillDepot) brand consisting of various labels, (think Barney Cotter, Ochre Crest, Slate Crest etc) I had an idea for the Cigar Rings for this project, where I put TM in an O (circle) of which I made mock ups (see attachement), now I am not a designer, I am sure a real designer can come up with something more stylish and unique.

```html
<!DOCTYPE html>
<html lang="en">
<head>
<meta charset="utf-8">
<title>TabacoMillDepot — Cigar Ring Concepts</title>
<link rel="stylesheet" href="https://fonts.googleapis.com/css2?family=Jost:wght@800&display=swap">
<style>
  :root {
    --paper: #ffffff;
    --red: #9b1e23;
    --red-deep: #6d1419;
    --black: #020202;
    --black-glow: #111111;
    --gold: #e3c45c;
    --ink-white: #ffffff;
  }
  * { margin: 0; padding: 0; box-sizing: border-box; }
  html, body {
    width: 1200px; height: 550px; overflow: hidden;
    background: var(--paper);
  }
  .sheet {
    position: relative; width: 1200px; height: 550px;
    font-family: "Jost", "Futura", sans-serif; font-weight: 800;
  }
  .ring {
    position: absolute; width: 560px; height: 225px;
  }
  .ring--top-left { left: 28px; top: 27px; }
  .ring--top-right { left: 611px; top: 27px; }
  .ring--bottom-left { left: 28px; top: 297px; }
  .ring--bottom-right { left: 611px; top: 297px; }

  .ring__edge-top { position: absolute; left: 0; right: 0; top: 0; height: 4px; }
  .ring__band { position: absolute; left: 0; right: 0; top: 18px; height: 184px;
    display: flex; align-items: center; justify-content: center; }
  .ring__edge-bottom { position: absolute; left: 0; right: 0; top: 216px; height: 9px; }

  .ring--red .ring__edge-top,
  .ring--red .ring__edge-bottom {
    background: linear-gradient(90deg, var(--red) 30%, var(--red-deep) 55%, var(--red) 80%);
  }
  .ring--red .ring__band {
    background: linear-gradient(120deg, var(--red) 30%, var(--red-deep) 50%, var(--red) 70%);
  }
  .ring--black .ring__edge-top,
  .ring--black .ring__edge-bottom { background: var(--black); }
  .ring--black .ring__band {
    background: linear-gradient(125deg, var(--black) 35%, var(--black-glow) 52%, var(--black) 70%);
  }

  .brand {
    display: flex; align-items: center; gap: 16px;
    color: var(--gold); letter-spacing: 0.06em; line-height: 1;
  }
  .brand__dot {
    width: 22px; height: 22px; border-radius: 50%; background: var(--gold);
  }
  .brand__name--full { font-size: 32px; }
  .brand__name--short { font-size: 64px; letter-spacing: 0.04em; }
</style>
</head>
<body>
<main class="sheet">
  <section class="ring ring--red ring--top-left">
    <div class="ring__edge-top"></div>
    <div class="ring__band">
      <div class="brand"><span class="brand__dot"></span><span class="brand__name brand__name--full">TabacoMillDepot</span></div>
    </div>
    <div class="ring__edge-bottom"></div>
  </section>

  <section class="ring ring--red ring--top-right">
    <div class="ring__edge-top"></div>
    <div class="ring__band">
      <div class="brand"><span class="brand__name brand__name--short">TMD</span></div>
    </div>
    <div class="ring__edge-bottom"></div>
  </section>

  <section class="ring ring--black ring--bottom-left">
    <div class="ring__edge-top"></div>
    <div class="ring__band">
      <div class="brand"><span class="brand__dot"></span><span class="brand__name brand__name--full">TabacoMillDepot</span></div>
    </div>
    <div class="ring__edge-bottom"></div>
  </section>

  <section class="ring ring--black ring--bottom-right">
    <div class="ring__edge-top"></div>
    <div class="ring__band">
      <div class="brand"><span class="brand__name brand__name--short">TMD</span></div>
    </div>
    <div class="ring__edge-bottom"></div>
  </section>
</main>
</body>
</html>
```